5 x 7 card advertising ash spreading

I need a new design for a double sided 5 x 7 horizontal post card to give to funeral homes so they can give them out to people who are interested in an ash spreading boat charter at sea for their loved one who has died. I want a simple, professional, classy, thoughtful design that I can include a summary of what we offer, what's included, our logo and and contact info. Even though we will include the "what" we offer, this piece needs to speak to the readers "why". I've included an AI excerpt about why people desire this as opposed to being buried.
What we offer: Attended service, Unattended service, Memorial service, Anniversary service. What's included: Certificate of Ash Spreading, Onboard refreshments, Personalized music. Our contact information: Tidewell Cruises, www.tidewellcruises.com, 412 Marlow Ave., Clearwater, FL 33761, (727) 584-9130

Target Market(s)

People visiting a funeral home planning their own or a relatives final wishes for ash spreading at sea

Industry/Entity Type

Private boat charters

Requirements
Must have
• Professional look, speaks to they "why", as well as includes the "what" we do.

```html
<!DOCTYPE html>
<html lang="en">
<head>
<meta charset="utf-8">
<title>Tidewell Cruises – Ash Spreading Postcard</title>
<link href="https://fonts.googleapis.com/css2?family=Bebas+Neue&family=Montserrat:wght@700;800&family=Poppins:wght@400;500;600;700&family=Yellowtail&display=block" rel="stylesheet">
<style>
  :root{
    --stage:#7b7b7b;
    --navy:#0b3f8c;
    --navy-deep:#0a2f6e;
    --sky:#22a7e6;
    --orange:#f28a30;
    --yellow:#f9c623;
    --ink:#2b2b2b;
    --white:#ffffff;
    --stamp:#c9c9c9;
    --rule:#c4c4c4;
  }
  *{margin:0;padding:0;box-sizing:border-box}
  html,body{width:935px;height:1200px;overflow:hidden}
  body{background:var(--stage);font-family:"Poppins",sans-serif;position:relative}
  .card{position:absolute;left:104px;width:727px;height:519px;background:var(--white);overflow:hidden}
  .card--front{top:45px}
  .card--back{top:616px}
  .abs{position:absolute}

  /* front */
  .hero-photo{left:0;top:0;width:727px;height:390px;
    background:linear-gradient(160deg,#cfe6f7 0%,#9fcdec 30%,#5fb8c9 55%,#3a9aa8 75%,#2f6f86 100%)}
  .title-panel{left:25px;top:61px;width:331px;height:320px;background:var(--navy);border-radius:30px 30px 0 0;opacity:.96}
  .brand{display:flex;align-items:center;gap:6px;font-family:"Montserrat",sans-serif;font-weight:800;font-size:17px;color:var(--white);white-space:nowrap}
  .brand__dot{width:14px;height:14px;border-radius:50%;background:var(--orange)}
  .brand--front{left:118px;top:62px}
  .title-main{left:59px;top:134px;font-family:"Bebas Neue",sans-serif;font-size:58px;line-height:1;color:var(--white);letter-spacing:-.5px;white-space:nowrap}
  .title-sub{left:59px;top:188px;font-family:"Montserrat",sans-serif;font-weight:800;font-size:30px;line-height:29px;color:var(--sky);white-space:nowrap}
  .title-script{left:62px;top:252px;font-family:"Yellowtail",cursive;font-size:38px;line-height:35px;color:var(--yellow);white-space:nowrap}
  .wave{left:0;top:0}
  .tag{background:var(--orange);color:var(--white);font-family:"Montserrat",sans-serif;font-weight:800;font-size:13.5px;line-height:20px;padding:0 6px;height:20px;white-space:nowrap}
  .tag--offer{left:57px;top:349px}
  .tag--included{left:424px;top:349px}
  .offer{position:absolute;top:378px;width:80px;text-align:center;font-size:11.5px;line-height:14px;color:var(--ink)}
  .offer svg{display:block;margin:0 auto 5px}
  .included{left:423px;top:375px;width:246px}
  .included li{list-style:none;height:23px;border:1.5px solid var(--sky);border-radius:2px;margin-bottom:2px;display:flex;align-items:center;gap:6px;padding-left:11px;font-weight:600;font-size:13px;color:var(--ink);white-space:nowrap}
  .phone-bar{left:0;top:464px;width:289px;height:52px;background:var(--navy);border-radius:0 8px 8px 0;display:flex;align-items:center;gap:12px;padding-left:58px;color:var(--white);font-weight:600;font-size:23px;white-space:nowrap}
  .contact{display:flex;align-items:center;gap:8px;font-size:14px;line-height:18px;color:var(--ink);white-space:nowrap}
  .contact--address{left:302px;top:469px}
  .contact--web{left:505px;top:475px}

  /* back */
  .back-art{left:0;top:0}
  .why-title{left:57px;top:22px;font-family:"Yellowtail",cursive;font-weight:400;font-size:29px;line-height:28px;color:var(--yellow);white-space:nowrap}
  .why-text{left:57px;top:92px;width:240px;font-size:10.2px;line-height:12.2px;color:var(--white)}
  .reasons-head{left:60px;top:155px;width:270px;font-family:"Montserrat",sans-serif;font-weight:800;font-size:12px;line-height:15px;color:var(--white)}
  .reason{position:absolute;left:55px;width:300px;display:flex;gap:6px}
  .reason__icon{flex:none;width:28px;height:28px;border-radius:50%;background:var(--navy);display:flex;align-items:center;justify-content:center}
  .reason__label{display:inline-block;background:var(--sky);color:var(--white);font-weight:600;font-size:10px;line-height:14px;padding:0 5px;border-radius:4px;white-space:nowrap}
  .reason__text{font-size:7.6px;line-height:9.4px;color:var(--ink);margin-top:2px}
  .phone-pill{left:54px;top:435px;height:24px;background:var(--sky);border-radius:8px;display:flex;align-items:center;gap:4px;padding:0 6px 0 3px;color:var(--white);font-weight:700;font-size:20px;white-space:nowrap}
  .phone-pill__icon{width:20px;height:20px;border-radius:50%;background:var(--yellow);display:flex;align-items:center;justify-content:center}
  .back-contact{left:56px;display:flex;align-items:center;gap:8px;font-size:13px;color:var(--white);white-space:nowrap}
  .brand--back{left:425px;top:66px;font-size:16px;color:var(--navy)}
  .stamp{left:609px;top:41px;width:69px;height:69px;background:var(--stamp)}
  .address-line{left:416px;width:264px;height:1.5px;background:var(--rule)}
</style>
</head>
<body>

<section class="card card--front">
  <div class="abs hero-photo" role="img" aria-label="Photo of a woman on a pontoon boat releasing ashes from her hands over turquoise sea under a bright sky"></div>
  <div class="abs title-panel"></div>
  <div class="abs brand brand--front"><span class="brand__dot"></span>Tidewell Cruises</div>
  <h1 class="abs title-main">ASH SPREADING</h1>
  <div class="abs title-sub">BOAT CHARTER<br>SERVICE AT SEA</div>
  <div class="abs title-script">for your loved one<br>who has died</div>

  <svg class="abs wave" width="727" height="519" viewBox="0 0 727 519">
    <path d="M0,385 C90,345 230,330 360,345 C470,358 620,340 727,300 L727,519 L0,519 Z" fill="#fff"/>
    <path d="M0,382 C90,342 230,327 360,342 C470,355 620,337 727,297" fill="none" stroke="#f28a30" stroke-width="3"/>
    <path d="M0,377 C90,337 230,322 360,337 C470,350 620,332 727,292" fill="none" stroke="#0a2f6e" stroke-width="2.5"/>
  </svg>

  <div class="abs tag tag--offer">WHAT WE OFFER</div>
  <div class="abs tag tag--included">WHAT'S INCLUDED</div>

  <div class="offer" style="left:44px">
    <svg width="33" height="33" viewBox="0 0 33 33"><circle cx="16.5" cy="16.5" r="16.5" fill="#0b3f8c"/><path d="M10 19h9l4-4M10 14h7" stroke="#fff" stroke-width="2" fill="none" stroke-linecap="round"/></svg>
    Attended<br>service
  </div>
  <div class="offer" style="left:119px">
    <svg width="33" height="33" viewBox="0 0 33 33"><circle cx="16.5" cy="16.5" r="16.5" fill="#0b3f8c"/><path d="M15 10h-4v13h4M14 16.5h9M19 12.5l4 4-4 4" stroke="#fff" stroke-width="2" fill="none" stroke-linecap="round" stroke-linejoin="round"/></svg>
    Unattended<br>service
  </div>
  <div class="offer" style="left:200px;top:379px">
    <svg width="33" height="33" viewBox="0 0 33 33"><circle cx="16.5" cy="16.5" r="16.5" fill="#0b3f8c"/><rect x="13" y="10" width="7" height="10" fill="#fff"/><rect x="9" y="21" width="15" height="3" fill="#fff"/></svg>
    Memorial<br>service
  </div>
  <div class="offer" style="left:273px;top:379px">
    <svg width="33" height="33" viewBox="0 0 33 33"><circle cx="16.5" cy="16.5" r="16.5" fill="#0b3f8c"/><path d="M10 24l4-11 7 7z" fill="#fff"/><circle cx="21" cy="11" r="1.5" fill="#fff"/><circle cx="24" cy="15" r="1.2" fill="#fff"/><circle cx="17" cy="9" r="1.2" fill="#fff"/></svg>
    Anniversary<br>service
  </div>

  <ul class="abs included">
    <li><svg width="9" height="9" viewBox="0 0 10 10"><circle cx="5" cy="5" r="5" fill="#0b3f8c"/><path d="M2.8 5.2l1.6 1.6 3-3" stroke="#fff" stroke-width="1.3" fill="none"/></svg>Certificate of Ash Spreading</li>
    <li><svg width="9" height="9" viewBox="0 0 10 10"><circle cx="5" cy="5" r="5" fill="#0b3f8c"/><path d="M2.8 5.2l1.6 1.6 3-3" stroke="#fff" stroke-width="1.3" fill="none"/></svg>Onboard refreshments</li>
    <li><svg width="9" height="9" viewBox="0 0 10 10"><circle cx="5" cy="5" r="5" fill="#0b3f8c"/><path d="M2.8 5.2l1.6 1.6 3-3" stroke="#fff" stroke-width="1.3" fill="none"/></svg>Personalized music</li>
  </ul>

  <div class="abs phone-bar">
    <svg width="18" height="18" viewBox="0 0 24 24"><path d="M6.6 10.8a15 15 0 006.6 6.6l2.2-2.2c.3-.3.7-.4 1-.2 1.1.4 2.3.6 3.6.6.6 0 1 .4 1 1V20c0 .6-.4 1-1 1A17 17 0 013 4c0-.6.4-1 1-1h3.5c.6 0 1 .4 1 1 0 1.3.2 2.5.6 3.6.1.3 0 .7-.2 1z" fill="#22a7e6"/></svg>
    (727) 584-9130
  </div>
  <div class="abs contact contact--address">
    <svg width="20" height="22" viewBox="0 0 20 22"><path d="M10 1a6 6 0 00-6 6c0 4.5 6 10 6 10s6-5.5 6-10a6 6 0 00-6-6z" fill="none" stroke="#0b3f8c" stroke-width="2"/><circle cx="10" cy="7" r="2" fill="#0b3f8c"/><ellipse cx="10" cy="19" rx="8" ry="2" fill="none" stroke="#0b3f8c" stroke-width="1.5"/></svg>
    <span>412 Marlow Ave.,<br>Clearwater, FL 33761</span>
  </div>
  <div class="abs contact contact--web">
    <svg width="20" height="20" viewBox="0 0 20 20"><circle cx="10" cy="10" r="8.5" fill="none" stroke="#0b3f8c" stroke-width="2"/><ellipse cx="10" cy="10" rx="3.5" ry="8.5" fill="none" stroke="#0b3f8c" stroke-width="1.5"/><path d="M2 10h16M3.5 6h13M3.5 14h13" stroke="#0b3f8c" stroke-width="1.3"/></svg>
    <span>www.tidewellcruises.com</span>
  </div>
</section>

<section class="card card--back">
  <svg class="abs back-art" width="727" height="519" viewBox="0 0 727 519">
    <defs>
      <clipPath id="leftPanel">
        <path d="M354,0 C380,40 400,100 396,160 C392,250 365,300 369,360 C372,430 385,480 398,519 L0,519 L0,0 Z"/>
      </clipPath>
      <linearGradient id="seaPhoto" x1="0" y1="0" x2="1" y2="1">
        <stop offset="0" stop-color="#0d2f8a"/>
        <stop offset=".5" stop-color="#1a5fb4"/>
        <stop offset="1" stop-color="#3d8fd0"/>
      </linearGradient>
    </defs>
    <g clip-path="url(#leftPanel)">
      <rect x="0" y="0" width="420" height="150" fill="url(#seaPhoto)" role="img" aria-label="Photo of a hand releasing ashes over a calm blue sea"/>
      <rect x="0" y="150" width="420" height="41" fill="#f28a30"/>
      <rect x="0" y="191" width="420" height="257" fill="#fff"/>
      <rect x="0" y="448" width="420" height="71" fill="#0b3f8c"/>
    </g>
    <path d="M354,0 C380,40 400,100 396,160 C392,250 365,300 369,360 C372,430 385,480 398,519" fill="none" stroke="#f28a30" stroke-width="3"/>
    <path d="M349,0 C375,40 395,100 391,160 C387,250 360,300 364,360 C367,430 380,480 393,519" fill="none" stroke="#0a2f6e" stroke-width="1.5"/>
  </svg>

  <h2 class="abs why-title">Why people choose to<br>scatter ashes at sea:</h2>
  <p class="abs why-text">People often choose to scatter ashes at sea because it symbolizes a deep connection to nature, representing a return to the elements and a sense of eternal continuity,</p>
  <div class="abs reasons-head">KEY REASONS WHY PEOPLE CHOOSE TO SCATTER ASHES AT SEA:</div>

  <div class="reason" style="top:197px">
    <div class="reason__icon"><svg width="14" height="14" viewBox="0 0 14 14"><path d="M7 8L3.5 4.5a2 2 0 013-2.6L7 2.4l.5-.5a2 2 0 013 2.6z" fill="#fff"/><path d="M2 10.5h10M2 12.5h10" stroke="#fff" stroke-width="1.2"/></svg></div>
    <div><span class="reason__label">Love for the Ocean</span>
    <p class="reason__text">Many people who enjoyed spending time on the water or had a career related to the sea find scattering ashes at sea a fitting tribute to their loved one's life</p></div>
  </div>
  <div class="reason" style="top:247px">
    <div class="reason__icon"><svg width="14" height="14" viewBox="0 0 14 14"><circle cx="7" cy="3" r="1.8" fill="#fff"/><path d="M7 5v4M3 12l4-3 4 3M2 8h10" stroke="#fff" stroke-width="1.2" fill="none"/></svg></div>
    <div><span class="reason__label">Symbolic Meaning</span>
    <p class="reason__text">The ocean represents vastness, eternity, and the constant flow of life, which can provide comfort and closure to grieving families.</p></div>
  </div>
  <div class="reason" style="top:287px">
    <div class="reason__icon"><svg width="14" height="14" viewBox="0 0 14 14"><path d="M7 2c2 2 2 4 0 6-2-2-2-4 0-6zM2 7c0 3 2 5 5 5s5-2 5-5" stroke="#fff" stroke-width="1.3" fill="none"/></svg></div>
    <div><span class="reason__label">Connection to Nature</span>
    <p class="reason__text">Scattering ashes at sea is viewed as a way to return a loved one to the natural world. becoming part of something larger than themselves.</p></div>
  </div>
  <div class="reason" style="top:335px">
    <div class="reason__icon"><svg width="14" height="14" viewBox="0 0 14 14"><rect x="2" y="2" width="10" height="10" rx="1.5" stroke="#fff" stroke-width="1.3" fill="none"/><circle cx="6.5" cy="6.5" r="2" stroke="#fff" stroke-width="1.2" fill="none"/><path d="M8 8l2 2" stroke="#fff" stroke-width="1.2"/></svg></div>
    <div><span class="reason__label">Sense of Release</span>
    <p class="reason__text">The act of scattering ashes can feel like a release, allowing the spirit of the deceased to be free and travel with the currents.</p></div>
  </div>
  <div class="reason" style="top:383px">
    <div class="reason__icon"><svg width="14" height="14" viewBox="0 0 14 14"><circle cx="7" cy="6" r="1.8" fill="#fff"/><path d="M4 9a4 4 0 010-6M10 9a4 4 0 000-6M7 8v5" stroke="#fff" stroke-width="1.2" fill="none"/></svg></div>
    <div><span class="reason__label">Spiritual Beliefs</span>
    <p class="reason__text">Some cultures and spiritual traditions associate the ocean with the afterlife or a journey to the next life.</p></div>
  </div>

  <div class="abs phone-pill">
    <span class="phone-pill__icon"><svg width="12" height="12" viewBox="0 0 24 24"><path d="M6.6 10.8a15 15 0 006.6 6.6l2.2-2.2c.3-.3.7-.4 1-.2 1.1.4 2.3.6 3.6.6.6 0 1 .4 1 1V20c0 .6-.4 1-1 1A17 17 0 013 4c0-.6.4-1 1-1h3.5c.6 0 1 .4 1 1 0 1.3.2 2.5.6 3.6.1.3 0 .7-.2 1z" fill="#0b3f8c"/></svg></span>
    (727) 584-9130
  </div>
  <div class="abs back-contact" style="top:464px">
    <svg width="13" height="15" viewBox="0 0 20 22"><path d="M10 1a6 6 0 00-6 6c0 4.5 6 10 6 10s6-5.5 6-10a6 6 0 00-6-6z" fill="none" stroke="#22a7e6" stroke-width="2"/><circle cx="10" cy="7" r="2" fill="#22a7e6"/></svg>
    412 Marlow Ave.,Clearwater, FL 33761
  </div>
  <div class="abs back-contact" style="top:481px">
    <svg width="13" height="13" viewBox="0 0 20 20"><circle cx="10" cy="10" r="8.5" fill="none" stroke="#22a7e6" stroke-width="2"/><ellipse cx="10" cy="10" rx="3.5" ry="8.5" fill="none" stroke="#22a7e6" stroke-width="1.5"/><path d="M2 10h16" stroke="#22a7e6" stroke-width="1.3"/></svg>
    www.tidewellcruises.com
  </div>

  <div class="abs brand brand--back"><span class="brand__dot"></span>Tidewell Cruises</div>
  <div class="abs stamp"></div>
  <div class="abs address-line" style="top:269px"></div>
  <div class="abs address-line" style="top:320px"></div>
  <div class="abs address-line" style="top:368px"></div>
</section>

</body>
</html>
```